Magnetic Business Card Design. One sided

Not happy yet with a design yet currently winning so far are the designs 5162585 5135573 5132280

Logo
unmatched Quality through traditional friendly service" sound like a good line. Blockages, Hot water units & all plumbing services.
7days,
free quote: 0491 275 634
Maybe put on it: Qualified, Licensed
www.brighttapplumbing.example.au

Make word as big so it is clearly able to be read

BrightTap Plumbing PTY LTD, target market is the middle aged mostly woman professional that owns a house and would rather pay a professional to do the job rather then a handyman.
We are a plumbing company based in Melbourne small and family owned with a focus on service to our customers.

I am after a design that is clean, professional and appealing to the eye which fits with the visual appearance of my web site and logo.

Our most profitable jobs are blockages and hot water units. however we do all types of plumbing. Maybe a point to make on the cards not sure tho.

I have included our previous magnet that i had designed with a pixel press template. if you can improve what we say to get new customers or totally change what is on the magnet. that would be fantastic.

I will also include other marketing material i have previously used

"unmatched Quality Through traditional friendly service" Could be a good catch line

These magnets are dropped into thousands of letter boxes and hopefully will find there way onto new clients fridges. Fridges in million dollar plus houses.

I really look forward to seeing your design. Thank you

Contact Information for Business Card

Number: 0491 275 634
Web site: www.Brighttapplumbing.example.au

```html
<!DOCTYPE html>
<html lang="en">
<head>
<meta charset="utf-8">
<title>BrightTap Plumbing – Magnetic Business Card</title>
<link rel="stylesheet" href="https://fonts.googleapis.com/css2?family=Ubuntu:wght@400;500;700&display=swap">
<style>
  :root {
    --page-bg: #eef0f2;
    --card-white: #ffffff;
    --brand-blue-light: #29abe2;
    --brand-blue-deep: #168bc8;
    --curve-blue: #1e9ad6;
    --tagline-blue: #3aa6dc;
    --brand-navy: #15275e;
    --text-dark: #1d2430;
    --text-light: #ffffff;
  }
  * { box-sizing: border-box; margin: 0; padding: 0; }
  html, body {
    width: 1200px;
    height: 900px;
    overflow: hidden;
    background: var(--page-bg);
    font-family: "Ubuntu", sans-serif;
  }
  .business-card {
    position: absolute;
    left: 75px;
    top: 150px;
    width: 1050px;
    height: 600px;
    background: var(--card-white);
    overflow: hidden;
  }
  .card-backdrop {
    position: absolute;
    inset: 0;
    width: 100%;
    height: 100%;
  }
  .credentials {
    position: absolute;
    left: 110px;
    top: 168px;
    width: 372px;
    text-align: center;
    font-size: 25px;
    color: var(--tagline-blue);
    white-space: nowrap;
  }
  .brand-lockup {
    position: absolute;
    left: 92px;
    top: 240px;
    width: 410px;
    display: flex;
    align-items: center;
    justify-content: center;
    gap: 16px;
  }
  .brand-mark {
    width: 22px;
    height: 22px;
    background: var(--brand-navy);
    flex-shrink: 0;
  }
  .brand-name {
    font-size: 48px;
    font-weight: 700;
    color: var(--brand-navy);
    line-height: 1.1;
    white-space: nowrap;
  }
  .service-pitch {
    position: absolute;
    left: 578px;
    top: 172px;
    font-size: 31px;
    line-height: 40px;
    color: var(--text-light);
    letter-spacing: 0.5px;
  }
  .call-prompt {
    position: absolute;
    left: 560px;
    top: 382px;
    width: 400px;
    text-align: center;
    font-size: 37px;
    font-weight: 700;
    letter-spacing: 5px;
    color: var(--text-dark);
  }
  .phone-number {
    position: absolute;
    left: 540px;
    top: 432px;
    font-size: 52px;
    letter-spacing: 4px;
    color: var(--text-light);
    white-space: nowrap;
  }
  .web-address {
    position: absolute;
    left: 496px;
    top: 496px;
    font-size: 26px;
    letter-spacing: 1px;
    color: var(--text-dark);
    white-space: nowrap;
  }
</style>
</head>
<body>
  <main class="business-card">
    <svg class="card-backdrop" viewBox="0 0 1050 600" aria-hidden="true">
      <defs>
        <linearGradient id="blueWash" x1="0" y1="0" x2="0" y2="1">
          <stop offset="0" stop-color="#29abe2"/>
          <stop offset="1" stop-color="#168bc8"/>
        </linearGradient>
      </defs>
      <path d="M526,0 L1050,0 L1050,600 L388,600 C470,520 532,400 542,262 C548,150 538,60 526,0 Z" fill="url(#blueWash)"/>
      <path d="M510,0 C521,60 529,150 525,262 C516,400 458,520 368,600" fill="none" stroke="#1e9ad6" stroke-width="7"/>
    </svg>

    <p class="credentials">Qualified | Licensed | Insured</p>

    <div class="brand-lockup">
      <span class="brand-mark"></span>
      <span class="brand-name">BrightTap<br>Plumbing</span>
    </div>

    <p class="service-pitch">Best plumbing services<br>at your doorsteps...<br>Why wait!</p>

    <p class="call-prompt">Call Now!</p>
    <p class="phone-number">0491 275 634</p>
    <p class="web-address">www.brighttapplumbing.example.au</p>
  </main>
</body>
</html>
```